Adventurous female pilot

I am looking for a personal business card, for a very well qualified female pilot, with a lot of aviation experience.

Currently an airline pilot, have worked as a bush pilot in Africa, looking to get into corporate aviation, or private jet owners.
Want a classy looking card for networking...

Could be interested in a retro\vintage look also?!

An idea,, is an african sunset background, with my wings\logo on it
Updates

I just want to say thank you to all of your for your amazing designs!

I have been very busy flying this past week , so not had a chance to be on the computer much.
But I provide some feedback, and conclusions very soon!
Thank you again.

Maren

Reason: Still waiting on a couple of revisions to be 100% about my choice!

Target Market(s)

corporate aviation, private jet owners, casino's,
General audience.
networking

Industry/Entity Type

Airline

Requirements
Nice to have
• Classy, edgy, sexy, but also feminine

```html
<!DOCTYPE html>
<html lang="en">
<head>
<meta charset="utf-8">
<title>Maren Castell Aviation – Business Card</title>
<link rel="stylesheet" href="https://fonts.googleapis.com/css2?family=Tenor+Sans&family=Arimo:wght@400&display=swap">
<style>
  :root {
    --sky-deep: #3c1212;
    --sky-mid: #a8120e;
    --sky-bright: #e8180f;
    --sky-warm: #f2462a;
    --ground: #050303;
    --ink-dark: #1c0707;
    --label-red: #ff2a1a;
    --value-white: #ffffff;
  }
  html, body {
    margin: 0;
    padding: 0;
    width: 1200px;
    height: 706px;
    overflow: hidden;
    background: #ffffff;
  }
  .card {
    position: relative;
    width: 1200px;
    height: 706px;
    overflow: hidden;
    font-family: "Tenor Sans", sans-serif;
  }
  .sunset-scene {
    position: absolute;
    left: 0;
    right: 0;
    top: 0;
    height: 532px;
    background: linear-gradient(115deg, var(--sky-deep) 0%, #761111 25%, var(--sky-mid) 45%, var(--sky-bright) 68%, var(--sky-warm) 100%);
  }
  .ground-band {
    position: absolute;
    left: 0;
    right: 0;
    top: 532px;
    bottom: 0;
    background: var(--ground);
  }
  .brand-mark {
    position: absolute;
    top: 140px;
    left: 0;
    width: 1236px;
    display: flex;
    justify-content: center;
    align-items: center;
    gap: 14px;
    color: var(--ink-dark);
    font-size: 40px;
    line-height: 1;
    letter-spacing: 6px;
  }
  .brand-mark .dot {
    width: 16px;
    height: 16px;
    border-radius: 50%;
    background: var(--ink-dark);
  }
  .identity {
    position: absolute;
    left: 483px;
    top: 320px;
    width: 288px;
    color: var(--ink-dark);
    text-align: right;
  }
  .identity .name {
    margin: 0;
    font-size: 42px;
    font-weight: 400;
    line-height: 1;
    white-space: nowrap;
  }
  .identity .division {
    margin: 10px 6px 0 0;
    font-size: 26px;
    letter-spacing: 1px;
    line-height: 1;
  }
  .contact {
    position: absolute;
    left: 0;
    top: 552px;
    font-family: "Arimo", sans-serif;
    font-size: 28px;
    line-height: 36px;
    border-collapse: collapse;
  }
  .contact td { padding: 0; white-space: nowrap; }
  .contact .label {
    color: var(--label-red);
    text-align: right;
    width: 257px;
    padding-right: 18px;
  }
  .contact .value { color: var(--value-white); }
</style>
</head>
<body>
  <main class="card">
    <div class="sunset-scene" role="img" aria-label="African sunset illustration: red sky with a setting sun, a soaring eagle, a jet on the runway, palms, giraffes and an elephant beneath an acacia tree"></div>
    <div class="ground-band"></div>

    <div class="brand-mark"><span class="dot"></span><span>AEROVEIL</span></div>

    <header class="identity">
      <h1 class="name">MAREN CASTELL</h1>
      <div class="division">AVIATION</div>
    </header>

    <table class="contact">
      <tr><td class="label">Cell US:</td><td class="value">+1 702-555-0143</td></tr>
      <tr><td class="label">Cell Taipei:</td><td class="value">+886 970-555-218</td></tr>
      <tr><td class="label">e-mail:</td><td class="value">marencastell@skymail.net</td></tr>
    </table>
  </main>
</body>
</html>
```